Dental Office Business Card

We need a business card for our pediatric dentistry office.
On one side the design needs to contain the following:
our logo (attached)
Corvin Pediatric Smiles
Tamsin Vetrakovich, DDS
Board Certified Pediatric Dentist
Tel: (617) 555-0148)
Fax: (617) 555-0193
Email: info@corvinpediatricsmiles.example
Web: www.corvinpediatricsmiles.example
Address: 42 Brambury Ln, Suite 208, Harrowgate, MA 01999

On the other side of the card, the design needs to have an appointment reminder (date and time as well as day of the week) similar to the design attached (no need for appointment reason “For”)

```html
<!DOCTYPE html>
<html lang="en">
<head>
<meta charset="utf-8">
<title>Corvin Pediatric Smiles – Business Card</title>
<link href="https://fonts.googleapis.com/css2?family=Marcellus&family=Montserrat:wght@400;500;600;700&display=swap" rel="stylesheet">
<style>
  :root {
    --bg: #3a3a3a;
    --card: #ffffff;
    --ink: #1e1e1e;
    --ink-soft: #3b3b3b;
    --mint: #a9d9ab;
    --line: #8f8f8f;
  }
  * { box-sizing: border-box; margin: 0; padding: 0; }
  html, body { width: 1200px; height: 875px; overflow: hidden; }
  body {
    background: var(--bg);
    font-family: "Montserrat", sans-serif;
    color: var(--ink);
    position: relative;
  }
  .card {
    position: absolute;
    top: 289px;
    width: 520px;
    height: 297px;
    background: var(--card);
    border-radius: 22px;
    overflow: hidden;
    box-shadow: 0 14px 30px rgba(0,0,0,.35);
  }
  .card--reminder { left: 60px; }
  .card--contact { left: 620px; }

  /* Appointment reminder side */
  .reminder-heading { position: absolute; top: 40px; left: 0; right: 0; text-align: center; }
  .reminder-heading__title {
    font-family: "Marcellus", serif;
    font-size: 26px;
    font-weight: 400;
    letter-spacing: 4px;
    color: var(--ink);
    line-height: 1;
  }
  .reminder-heading__sub {
    font-size: 20px;
    font-weight: 500;
    color: var(--mint);
    line-height: 1.1;
  }
  .field { position: absolute; left: 40px; right: 40px; display: flex; align-items: flex-end; font-size: 15px; font-weight: 600; color: var(--ink-soft); }
  .field--date { top: 140px; }
  .field--time { top: 184px; }
  .field__label { white-space: nowrap; margin-right: 10px; }
  .field__rule { flex: 1; border-bottom: 1px solid var(--line); margin-bottom: 4px; }
  .field__suffix { margin-left: 8px; font-weight: 500; font-size: 14px; }
  .weekdays { position: absolute; left: 40px; right: 30px; top: 236px; display: flex; justify-content: space-between; list-style: none; }
  .weekday { display: flex; align-items: center; gap: 6px; font-family: "Marcellus", serif; font-size: 14px; letter-spacing: 1px; color: var(--ink-soft); }
  .weekday__box { width: 15px; height: 15px; border: 1px solid var(--ink-soft); }

  /* Contact side */
  .brand { position: absolute; top: 44px; left: 0; right: 0; display: flex; align-items: center; justify-content: center; gap: 12px; }
  .brand__dot { width: 30px; height: 30px; border-radius: 50%; background: var(--mint); }
  .brand__name { font-size: 24px; font-weight: 700; color: var(--ink); letter-spacing: .3px; }
  .person { position: absolute; left: 28px; top: 142px; width: 230px; text-align: right; }
  .person__name { font-size: 17px; font-weight: 600; color: var(--mint); line-height: 1.2; }
  .person__title { font-size: 11.5px; font-weight: 500; color: var(--ink-soft); margin-top: 4px; }
  .divider { position: absolute; left: 270px; top: 122px; width: 1px; height: 96px; background: var(--mint); }
  .contacts { position: absolute; left: 284px; top: 126px; list-style: none; }
  .contacts__item { display: flex; align-items: center; gap: 7px; font-size: 11px; font-weight: 500; color: var(--ink-soft); line-height: 22px; white-space: nowrap; }
  .contacts__icon { width: 11px; height: 11px; flex: none; }
  .band { position: absolute; left: 0; right: 0; top: 236px; height: 34px; background: var(--mint); display: flex; align-items: center; justify-content: flex-end; padding-right: 30px; }
  .band__address { font-size: 12px; font-weight: 500; color: #fff; white-space: nowrap; }
</style>
</head>
<body>

<section class="card card--reminder" aria-label="Appointment reminder side">
  <header class="reminder-heading">
    <h1 class="reminder-heading__title">APPOINTMENT</h1>
    <p class="reminder-heading__sub">Reminder</p>
  </header>
  <div class="field field--date"><span class="field__label">Date :</span><span class="field__rule"></span></div>
  <div class="field field--time"><span class="field__label">Time :</span><span class="field__rule"></span><span class="field__suffix">am/pm</span></div>
  <ul class="weekdays">
    <li class="weekday"><span class="weekday__box"></span>Mon</li>
    <li class="weekday"><span class="weekday__box"></span>Tue</li>
    <li class="weekday"><span class="weekday__box"></span>Wed</li>
    <li class="weekday"><span class="weekday__box"></span>Thu</li>
    <li class="weekday"><span class="weekday__box"></span>Fri</li>
    <li class="weekday"><span class="weekday__box"></span>Sat</li>
    <li class="weekday"><span class="weekday__box"></span>Sun</li>
  </ul>
</section>

<section class="card card--contact" aria-label="Contact side">
  <div class="brand">
    <span class="brand__dot"></span>
    <span class="brand__name">Corvin Pediatric Smiles</span>
  </div>
  <div class="person">
    <p class="person__name">Tamsin Vetrakovich, DDS</p>
    <p class="person__title">Board Certified Pediatric Dentist</p>
  </div>
  <span class="divider"></span>
  <ul class="contacts">
    <li class="contacts__item">
      <svg class="contacts__icon" viewBox="0 0 24 24"><path fill="#a9d9ab" d="M6.6 10.8a15 15 0 0 0 6.6 6.6l2.2-2.2a1 1 0 0 1 1-.25 11.4 11.4 0 0 0 3.6.57 1 1 0 0 1 1 1V20a1 1 0 0 1-1 1A17 17 0 0 1 3 4a1 1 0 0 1 1-1h3.5a1 1 0 0 1 1 1c0 1.25.2 2.450.57 3.57a1 1 0 0 1-.25 1z"/></svg>
      (617) 555-0148)
    </li>
    <li class="contacts__item">
      <svg class="contacts__icon" viewBox="0 0 24 24"><path fill="#a9d9ab" d="M6 3h10v5H6zM3 9h18v9h-3v3H6v-3H3zm5 7v3h8v-3z"/></svg>
      (617) 555-0193
    </li>
    <li class="contacts__item">
      <svg class="contacts__icon" viewBox="0 0 24 24"><path fill="#a9d9ab" d="M2 5h20v14H2zm2 2v.5l8 5 8-5V7l-8 5z"/></svg>
      info@corvinpediatricsmiles.example
    </li>
    <li class="contacts__item">
      <svg class="contacts__icon" viewBox="0 0 24 24"><circle cx="12" cy="12" r="9" fill="none" stroke="#a9d9ab" stroke-width="2"/><path d="M3 12h18M12 3c3 3 3 15 0 18M12 3c-3 3-3 15 0 18" fill="none" stroke="#a9d9ab" stroke-width="1.6"/></svg>
      www.corvinpediatricsmiles.example
    </li>
  </ul>
  <div class="band"><span class="band__address">42 Brambury Ln, Suite 208, Harrowgate, MA 01999</span></div>
</section>

</body>
</html>
```